Business Card Design

Its a residential construction company

Industry/Entity Type

Residential

Contact Information for Business Card

Belvora Homes Pty Ltd,
Dylan R Foster
BE (Civil), Grad.Dip Hwy, Eng. (QCTU), FTC.Aust,
Director, Belvora Homes Pty Ltd

PO Box 587, Tallowvale, NSW, 2599. Tel: 048765 2231
email: dylan@belvorahomes.com

```html
<!DOCTYPE html>
<html lang="en">
<head>
<meta charset="utf-8">
<title>Belvora Homes Pty Ltd — Business Card</title>
<link rel="stylesheet" href="https://fonts.googleapis.com/css2?family=Ubuntu:wght@400;500;700&display=swap">
<style>
  :root {
    --bg: #e9ebea;
    --card-white: #ffffff;
    --brand-green: #06b98f;
    --text-on-green: #ffffff;
    --shadow: rgba(0, 0, 0, 0.18);
  }
  * { box-sizing: border-box; margin: 0; padding: 0; }
  html, body {
    width: 1200px;
    height: 1000px;
    overflow: hidden;
    background: var(--bg);
    font-family: "Ubuntu", sans-serif;
  }
  .stage {
    width: 1200px;
    height: 1000px;
    display: flex;
    align-items: center;
    justify-content: center;
  }
  .business-card {
    width: 1000px;
    height: 600px;
    display: flex;
    box-shadow: 0 14px 40px var(--shadow);
  }
  .brand-panel {
    width: 370px;
    background: var(--card-white);
    display: flex;
    flex-direction: column;
    align-items: center;
    justify-content: center;
    gap: 22px;
    padding: 40px;
  }
  .brand-mark {
    width: 56px;
    height: 56px;
    background: var(--brand-green);
  }
  .brand-name {
    color: var(--brand-green);
    font-weight: 500;
    font-size: 30px;
    letter-spacing: 3px;
    text-transform: uppercase;
    text-align: center;
    line-height: 1.35;
  }
  .details-panel {
    flex: 1;
    background: var(--brand-green);
    color: var(--text-on-green);
    text-align: right;
    padding: 56px 52px 52px 40px;
    display: flex;
    flex-direction: column;
    justify-content: space-between;
  }
  .person-name {
    font-weight: 700;
    font-size: 34px;
    margin-bottom: 26px;
  }
  .credentials,
  .role,
  .company {
    font-size: 23px;
    line-height: 1.3;
  }
  .credentials { margin-bottom: 18px; }
  .contact-block {
    font-size: 24px;
    line-height: 1.45;
    font-style: normal;
  }
</style>
</head>
<body>
  <main class="stage">
    <article class="business-card">
      <section class="brand-panel">
        <div class="brand-mark" aria-hidden="true"></div>
        <div class="brand-name">Belvora Homes<br>Pty Ltd</div>
      </section>
      <section class="details-panel">
        <header class="identity">
          <h1 class="person-name">Dylan R Foster</h1>
          <p class="credentials">BE (Civil), Grad.Dip Hwy, Eng. (QCTU), FTC.Aust</p>
          <p class="role">Director</p>
          <p class="company">Belvora Homes Pty Ltd</p>
        </header>
        <address class="contact-block">
          <p class="postal">PO Box 587, Tallowvale, NSW, 2599</p>
          <p class="phone">Tel: 048765 2231</p>
          <p class="email">Email: dylan@belvorahomes.com</p>
        </address>
      </section>
    </article>
  </main>
</body>
</html>
```